Business Card Design Project

Our slogan is "Built to stand apart" and we are after something creative and different to go with our company image.

Criteria:
The business card will not be a standard size but it must be small or big enough to fit in a wallet.
It will be double sided
It will have our colours and the design will be based around our logo (attached)
No fancy text just clean sharp easy to read. we have been using the stag sans book font type so this or similar type is preferable (we are not locked in a font type.

For more information about us, please visit out website at www.tovelmarsh.com.au

Target Market(s)

outdoor and recreational industry/market

Industry/Entity Type

Business

Requirements
Must have
• Logo
Slogan
website
contact details (phone and email)
Name and Position
social media facebook and youtube

```html
<!DOCTYPE html>
<html lang="en">
<head>
<meta charset="utf-8">
<title>Tovel Marsh Business Card</title>
<link rel="stylesheet" href="https://fonts.googleapis.com/css2?family=Arimo:wght@400;700&display=swap">
<style>
  :root {
    --page-bg: #ece9e5;
    --card-dark: #232326;
    --card-dark-glow: #2d2d31;
    --card-light: #ffffff;
    --accent: #e8502c;
    --ink: #2a2a2a;
    --ink-soft: #333333;
    --white: #ffffff;
    --tile-blue: #3b6fb6;
    --tile-red: #9a3a2a;
  }
  * { margin: 0; padding: 0; box-sizing: border-box; }
  html, body {
    width: 960px; height: 1200px; overflow: hidden;
    background: var(--page-bg);
    font-family: "Arimo", Arial, sans-serif;
  }
  .canvas { position: relative; width: 960px; height: 1200px; }
  .card {
    position: absolute; left: 136px; width: 694px; height: 376px;
    border-radius: 16px; overflow: hidden;
    box-shadow: 0 6px 18px rgba(0,0,0,0.18);
  }
  /* Front */
  .card-front {
    top: 195px;
    background: radial-gradient(ellipse at 50% 40%, var(--card-dark-glow) 0%, var(--card-dark) 60%);
  }
  .front-ring {
    position: absolute; left: 244px; top: 24px; width: 208px; height: 208px;
    border: 4px solid var(--accent); border-radius: 50%;
  }
  .front-name {
    position: absolute; left: 0; right: 0; top: 250px; text-align: center;
    color: var(--white); font-size: 38px; font-weight: 400; letter-spacing: 2px;
    white-space: nowrap;
  }
  .front-slogan {
    position: absolute; left: 0; right: 0; top: 302px; text-align: center;
    color: var(--white); font-size: 14px; font-weight: 700; letter-spacing: 2.5px;
    text-transform: uppercase; white-space: nowrap;
  }
  .web-band {
    position: absolute; left: 0; right: 0; bottom: 0; height: 32px;
    background: var(--accent); color: var(--white);
    font-size: 17px; letter-spacing: 3px; text-transform: uppercase;
    display: flex; align-items: center; justify-content: center;
    white-space: nowrap;
  }
  /* Back */
  .card-back { top: 630px; background: var(--card-light); }
  .back-ring {
    position: absolute; left: 344px; top: 38px; width: 80px; height: 80px;
    border: 3px solid var(--accent); border-radius: 50%;
  }
  .back-name {
    position: absolute; left: 440px; top: 60px;
    color: var(--ink); font-size: 30px; font-weight: 400; letter-spacing: 1px;
    white-space: nowrap;
  }
  .person-name {
    position: absolute; left: 62px; top: 112px;
    font-size: 27px; font-weight: 700; color: var(--ink); white-space: nowrap;
  }
  .person-name .surname { color: var(--accent); }
  .person-role {
    position: absolute; left: 62px; top: 146px;
    font-size: 14px; font-weight: 700; color: var(--ink);
  }
  .info-block {
    position: absolute; top: 198px;
    font-size: 16px; line-height: 21px; color: var(--ink-soft); white-space: nowrap;
  }
  .info-block .label { font-weight: 700; }
  .info-address { left: 88px; }
  .info-contact { left: 406px; }
  .social-row {
    position: absolute; top: 334px; display: flex; align-items: center; gap: 14px;
    font-size: 11px; letter-spacing: 1.4px; text-transform: uppercase; color: var(--ink-soft);
    white-space: nowrap;
  }
  .social-row .handle { color: var(--accent); }
  .social-icon { width: 24px; height: 24px; border-radius: 3px; }
  .social-community { left: 40px; }
  .social-community .social-icon { background: var(--tile-blue); }
  .social-videos { left: 360px; }
  .social-videos .social-icon { background: var(--tile-red); }
</style>
</head>
<body>
<main class="canvas">
  <section class="card card-front" aria-label="Card front">
    <div class="front-ring"></div>
    <div class="front-name">TOVEL MARSH</div>
    <div class="front-slogan">Built to stand apart</div>
    <div class="web-band">http://www.tovelmarsh.com.au</div>
  </section>

  <section class="card card-back" aria-label="Card back">
    <div class="back-ring"></div>
    <div class="back-name">TOVEL MARSH</div>

    <div class="person-name">Mara <span class="surname">Quill</span></div>
    <div class="person-role">Director</div>

    <div class="info-block info-address">
      <div class="label">Office Address:</div>
      <div>14/52 Hollis Lane, Brindle Park</div>
      <div>4120 Queensland, Australia</div>
    </div>

    <div class="info-block info-contact">
      <div class="label">Email:</div>
      <div>enquiries@tovelmarsh.com.au</div>
      <div class="label">Phone:</div>
      <div>00 456 7810</div>
    </div>

    <div class="social-row social-community">
      <span class="social-icon"></span>
      <span>www.tovelmarsh.com.au/<span class="handle">Community</span></span>
    </div>
    <div class="social-row social-videos">
      <span class="social-icon"></span>
      <span>www.tovelmarsh.com.au/The<span class="handle">Videos</span></span>
    </div>
  </section>
</main>
</body>
</html>
```